Bref créative
Stationary for Stonebrook Putting Institute
Driving range/Golf Academy
Simple
Pieter de Groenhout
Director of Golfschool
P.O. Box 48306
00452 Nairobi
pieter@stonebrookputt.co.ke
www.stonebrookputt.com
I am a TCA Professional from Holland and the logo off the TCA Holland should be incorporated at the business card. You can download it from the internet.
We have 2 other people who need business cards, Wilhelmina Drostraat CEO
Tom Wanjau Director
These two no TCA LOGO
Business card with black back ground, and for Pieter de Groenhout inclusive TCA Holland logo,
Letterhead the white background

```html
<!DOCTYPE html>
<html lang="en">
<head>
<meta charset="utf-8">
<title>Stonebrook Putting Institute — Business Card</title>
<link rel="stylesheet" href="https://fonts.googleapis.com/css2?family=Roboto:wght@400;700&family=Roboto+Condensed:wght@700&display=swap">
<style>
  :root {
    --stage: #2b2b2b;
    --card-black: #0c0c0c;
    --card-charcoal: #1c1c1c;
    --brand-red: #d3141c;
    --deep-red: #7a0a0e;
    --white: #ffffff;
    --soft-white: #e6e6e6;
  }
  * { margin: 0; padding: 0; box-sizing: border-box; }
  html, body {
    width: 1200px; height: 901px; overflow: hidden;
    background: var(--stage);
    font-family: "Roboto", Arial, sans-serif;
  }
  .business-card {
    position: absolute; left: 100px; top: 165px;
    width: 1000px; height: 571px;
    background: linear-gradient(135deg, var(--card-charcoal) 0%, var(--card-black) 60%);
    overflow: hidden;
    box-shadow: 0 20px 50px rgba(0,0,0,.45);
  }
  .card-wave { position: absolute; inset: 0; width: 100%; height: 100%; }
  .brand {
    position: absolute; left: 150px; top: 205px;
    display: flex; align-items: center; gap: 22px;
  }
  .brand-mark {
    width: 74px; height: 74px; border-radius: 50%;
    background: var(--brand-red);
  }
  .brand-name {
    font-family: "Roboto Condensed", "Arial Narrow", sans-serif;
    font-weight: 700; font-size: 40px; line-height: 1.05;
    color: var(--white); letter-spacing: .5px;
  }
  .holder {
    position: absolute; left: 150px; top: 360px;
  }
  .holder-name {
    font-size: 26px; font-weight: 700; color: var(--brand-red);
  }
  .holder-role {
    margin-top: 6px; font-size: 16px; color: var(--soft-white);
  }
  .contact {
    position: absolute; right: 48px; top: 175px;
    text-align: right; color: var(--white); font-size: 17px; line-height: 1.55;
  }
  .contact-address { margin-bottom: 22px; }
  .contact-line {
    display: flex; justify-content: flex-end; align-items: center; gap: 10px;
  }
  .contact-icon { width: 16px; height: 16px; flex: none; }
</style>
</head>
<body>
  <main class="business-card">
    <svg class="card-wave" viewBox="0 0 1000 571" preserveAspectRatio="none" aria-hidden="true">
      <defs>
        <linearGradient id="waveRed" x1="0" y1="1" x2="1" y2="0">
          <stop offset="0" stop-color="#8e0b10"/>
          <stop offset=".55" stop-color="#d3141c"/>
          <stop offset="1" stop-color="#e8262c"/>
        </linearGradient>
      </defs>
      <path d="M520 571 C660 470 600 250 730 130 C800 65 900 30 1000 10 L1000 571 Z" fill="var(--deep-red)"/>
      <path d="M540 571 C680 475 625 260 750 145 C815 85 905 50 1000 32" fill="none" stroke="var(--white)" stroke-width="5"/>
      <path d="M565 571 C700 480 650 275 770 160 C830 100 910 68 1000 52 L1000 571 Z" fill="url(#waveRed)"/>
    </svg>

    <div class="brand">
      <span class="brand-mark"></span>
      <span class="brand-name">Stonebrook<br>Putting Institute</span>
    </div>

    <div class="holder">
      <p class="holder-name">Pieter de Groenhout</p>
      <p class="holder-role">Director of Golfschool</p>
    </div>

    <address class="contact" style="font-style:normal">
      <p class="contact-address">P.O. Box 48306<br>00452 Nairobi</p>
      <p class="contact-line">
        <svg class="contact-icon" viewBox="0 0 24 24"><path fill="#fff" d="M6.6 10.8a15 15 0 0 0 6.6 6.6l2.2-2.2c.3-.3.7-.4 1-.2 1.1.4 2.3.6 3.6.6.6 0 1 .4 1 1V20c0 .6-.4 1-1 1A17 17 0 0 1 3 4c0-.6.4-1 1-1h3.5c.6 0 1 .4 1 1 0 1.3.2 2.5.6 3.6.1.3 0 .7-.2 1z"/></svg>
        <span>+254 712 408 615</span>
      </p>
      <p class="contact-line">
        <svg class="contact-icon" viewBox="0 0 24 24"><rect x="2" y="5" width="20" height="14" rx="1.5" fill="#fff"/><path d="M3 6l9 7 9-7" fill="none" stroke="#b00f15" stroke-width="2"/></svg>
        <span>pieter@stonebrookputt.co.ke</span>
      </p>
      <p class="contact-line">
        <svg class="contact-icon" viewBox="0 0 24 24"><circle cx="12" cy="12" r="9.5" fill="none" stroke="#fff" stroke-width="2"/><path d="M2.5 12h19M12 2.5c3 3 3 16 0 19M12 2.5c-3 3-3 16 0 19" fill="none" stroke="#fff" stroke-width="1.6"/></svg>
        <span>www.stonebrookputt.com</span>
      </p>
    </address>
  </main>
</body>
</html>
```